Enter the secret world of social tradecraft

Design a stunning work of art that markets our product "Quillmark: A Hidden Ledger of Social Outreach Methods"

We need a set of assets for using in building our wordpress site and marketing materials. We'd like to have those assets delivered as a ONE PAGE HTML5 LANDING PAGE example.

We have a video that gives the look and feel of that we are going for and would like to extend it into a landing page for now with a customized logo to be included.

Watch the video here: https://www.vidloom-example.net/watch?v=QpRtLmN_7W2

The product is an informational product containing information on ZV marketing.

The final design should be intriguing and draw in the user with hints of intrigue.

Target Market(s)

Online Marketers

Industry/Entity Type

Marketing

Requirements
Must have
• Must match video in look and feel; must be html5 and responsive
Nice to have
• inventive html animations or css transitions

```html
<!DOCTYPE html>
<html lang="en">
<head>
<meta charset="utf-8">
<title>Quillmark — A Hidden Ledger of Social Outreach Methods</title>
<link href="https://fonts.googleapis.com/css2?family=Almendra&family=Raleway:wght@300;400;600&display=swap" rel="stylesheet">
<style>
:root{
  --ink:#000;
  --char:#2e2e2e;
  --foot:#2b2b2b;
  --soft:#bdbdbd;
  --mute:#9a9a9a;
  --pale:#e4e4e4;
  --rule:#4a4a4a;
  --display:'Almendra', serif;
  --body:'Raleway', sans-serif;
}
*{margin:0;padding:0;box-sizing:border-box}
html,body{width:702px;height:1200px;overflow:hidden;background:var(--ink)}
body{position:relative;font-family:var(--body);color:var(--soft)}
.abs{position:absolute}

/* hero */
.hero{left:0;top:0;width:702px;height:394px;background:var(--ink)}
.hero-photo{left:0;top:0;width:330px;height:394px;
  background:radial-gradient(ellipse at 45% 55%,#5a5a5a 0%,#2a2a2a 45%,#000 80%)}
.logo-panel{left:0;top:0;width:366px;height:189px;
  background:radial-gradient(ellipse at 50% 50%,#3a3a3a 0%,#1c1c1c 60%,#111 100%)}
.brand{left:44px;top:52px;font-family:var(--display);font-size:54px;color:var(--pale);letter-spacing:2px}
.nav{left:343px;top:118px;display:flex;gap:25px;font-size:15.5px;font-weight:300;color:var(--soft)}
.headline{left:337px;top:210px;font-family:var(--display);font-size:25px;line-height:31px;color:var(--pale)}
.tagline{left:338px;top:296px;font-family:var(--display);font-size:16px;line-height:20px;color:var(--pale)}

/* offer */
.offer{left:0;top:394px;width:702px;height:328px;background:var(--char)}
.offer-art{left:140px;top:470px;width:480px;height:255px;
  background:radial-gradient(ellipse at 50% 55%,#4a4a4a 0%,#393939 50%,rgba(46,46,46,0) 80%);opacity:.7}
.section-title{font-family:var(--display);color:var(--pale);letter-spacing:1px}
.offer-title{left:26px;top:436px;font-size:31px}
.feature{display:flex;align-items:center;gap:14px}
.feature svg{width:38px;height:40px;flex:none}
.feature-text{font-size:19px;font-weight:300;line-height:26px;color:var(--mute);text-transform:uppercase}

/* about */
.about{left:0;top:722px;width:702px;height:270px;background:var(--ink)}
.about-art{left:133px;top:722px;width:469px;height:260px;
  background:linear-gradient(160deg,#1e1e1e 0%,#141414 50%,#1b1b1b 100%)}
.about-title{left:0;top:778px;width:702px;text-align:center;font-size:24px}
.about-copy{left:50px;top:834px;width:602px;text-align:center;font-size:18px;font-weight:300;line-height:26px;color:var(--mute)}

/* footer */
.footer{left:0;top:992px;width:702px;height:208px;background:var(--foot)}
.foot-brand{left:30px;top:1048px;font-family:var(--display);font-size:30px;color:var(--pale);letter-spacing:1px}
.foot-links{left:225px;top:1030px;list-style:none;font-size:12px;line-height:21.5px;color:var(--pale)}
.map{left:368px;top:1026px;width:150px;height:82px;border:1px solid #888;
  background:linear-gradient(135deg,#d8d8d8,#bdbdbd)}
.contact{left:527px;top:1027px;color:var(--pale)}
.office{font-size:9px;font-weight:600}
.address{font-size:8.5px;margin-top:2px}
.contact-line{display:flex;align-items:center;gap:6px;margin-top:6px}
.contact-line svg{width:18px;height:18px}
.phone{font-size:17px}
.email{font-size:12.5px}
.foot-rule{left:29px;top:1146px;width:635px;height:1px;background:var(--rule)}
.copyright{left:29px;top:1162px;font-size:8.5px;line-height:11px;color:var(--pale)}
.social{left:546px;top:1162px;display:flex;gap:6px}
.social span{width:20px;height:20px;border-radius:50%;background:#e4e4e4;display:block}
</style>
</head>
<body>

<section class="hero abs">
  <div class="hero-photo abs" role="img" aria-label="Black and white photo of a man in a fedora and trench coat"></div>
  <div class="logo-panel abs"></div>
  <div class="brand abs">Quillmark</div>
  <nav class="nav abs"><span>HOME</span><span>ABOUT</span><span>SERVICES</span><span>CONTACT US</span></nav>
  <h1 class="headline abs" style="font-weight:400">A Hidden Ledger of<br>Social Outreach Methods</h1>
  <p class="tagline abs">Informational product containing<br>information on ZV marketing</p>
</section>

<section class="offer abs"></section>
<div class="offer-art abs" role="img" aria-label="Faint sketched anatomical figure drawing"></div>
<h2 class="section-title offer-title abs" style="font-weight:400">WHAT WE OFFER</h2>

<div class="feature abs" style="left:56px;top:543px">
  <svg viewBox="0 0 38 40" fill="none" stroke="#9a9a9a" stroke-width="2.5"><path d="M19 3a12 12 0 0 0-7 21.5V30h14v-5.5A12 12 0 0 0 19 3z"/><path d="M13 34h12M15 38h8"/><circle cx="19" cy="13" r="3" fill="#9a9a9a"/><path d="M15 25v-5h8v5" fill="#9a9a9a"/></svg>
  <div class="feature-text">Techniques to<br>acquire intelligence</div>
</div>
<div class="feature abs" style="left:388px;top:543px">
  <svg viewBox="0 0 38 40" fill="#9a9a9a"><circle cx="8" cy="11" r="3"/><rect x="5" y="15" width="6" height="12"/><circle cx="19" cy="8" r="3.5"/><rect x="15.5" y="13" width="7" height="15"/><circle cx="30" cy="11" r="3"/><rect x="27" y="15" width="6" height="12"/><ellipse cx="19" cy="33" rx="16" ry="4" fill="none" stroke="#9a9a9a" stroke-width="2.5"/></svg>
  <div class="feature-text">Learn the<br>social black art</div>
</div>
<div class="feature abs" style="left:56px;top:636px">
  <svg viewBox="0 0 38 40" fill="#9a9a9a"><rect x="2" y="2" width="34" height="20" fill="none" stroke="#9a9a9a" stroke-width="2.5"/><rect x="8" y="12" width="3" height="7"/><rect x="14" y="9" width="3" height="10"/><rect x="20" y="6" width="3" height="13"/><circle cx="7" cy="29" r="3"/><rect x="3" y="33" width="8" height="6"/><circle cx="19" cy="29" r="3"/><rect x="15" y="33" width="8" height="6"/><circle cx="31" cy="29" r="3"/><rect x="27" y="33" width="8" height="6"/></svg>
  <div class="feature-text">Devise clandestine<br>strategies</div>
</div>
<div class="feature abs" style="left:388px;top:636px">
  <svg viewBox="0 0 38 40" fill="none" stroke="#9a9a9a" stroke-width="2.5"><rect x="2" y="5" width="34" height="24"/><path d="M13 35h12M19 29v6"/><circle cx="19" cy="17" r="5"/><circle cx="19" cy="17" r="1.5" fill="#9a9a9a"/></svg>
  <div class="feature-text">Decipher cryptic<br>patterns</div>
</div>

<section class="about abs"></section>
<div class="about-art abs" role="img" aria-label="Dark textured grid of crossing light lines"></div>
<h2 class="section-title about-title abs" style="font-weight:400">WHAT EXACTLY IS QUILLMARK?</h2>
<p class="about-copy abs">Ut wisi enim ad minim veniam, quis nostrud exerci tation ullamcorper suscipit lobortis nisl ut aliquip ex ea commodo consequat. Duis autem vel eum iriure dolor in hendrerit in vulputate velit esse molestie consequat, vel illum dolore eu feugiat nulla facilisis at vero eros et accumsan.</p>

<footer class="footer abs"></footer>
<div class="foot-brand abs">Quillmark</div>
<ul class="foot-links abs"><li>Home</li><li>About</li><li>Services</li><li>Contact</li></ul>
<div class="map abs" role="img" aria-label="Street map showing the office location"></div>
<div class="contact abs">
  <div class="office">Main Office:</div>
  <div class="address">Level 4, 17 Wren Lane, Eastbrook</div>
  <div class="contact-line">
    <svg viewBox="0 0 18 18" fill="none" stroke="#e4e4e4" stroke-width="1.4"><circle cx="9" cy="9" r="8"/><path d="M6 5l2 2-1 1.5c.7 1.4 1.6 2.3 3 3l1.5-1 2 2-1.5 1.5c-3 0-7-4-7-7z" fill="#e4e4e4"/></svg>
    <span class="phone">03 5550 1298</span>
  </div>
  <div class="contact-line">
    <svg viewBox="0 0 18 18" fill="none" stroke="#e4e4e4" stroke-width="1.4"><circle cx="9" cy="9" r="8"/><rect x="4.5" y="6" width="9" height="6"/><path d="M4.5 6l4.5 3.5L13.5 6"/></svg>
    <span class="email">hello@quillmark-example.net</span>
  </div>
</div>
<div class="foot-rule abs"></div>
<p class="copyright abs">Copyright © 2014 Harbourline Media Pty.<br>All rights reserved.</p>
<div class="social abs"><span></span><span></span><span></span><span></span><span></span></div>

</body>
</html>
```